Harborline Frame Construction Needs business card

Hey we are in need of business card designs. I have upload our logo as a guideline, but free feel to run with it or come up with something unique.
Pls have fun with it and be creative. the name says it all!
i will give some directions after i see a few entries..
Logo source file has been uploaded..
Hey because of the logo is so colourful already.
Can we have a few submissions with less colour.
Also we are looking for clever/hidden/descriptive business card.

```html
<!DOCTYPE html>
<html lang="en">
<head>
<meta charset="utf-8">
<title>Harborline Frame Construction – Business Card</title>
<link rel="stylesheet" href="https://fonts.googleapis.com/css2?family=Questrial&family=Josefin+Sans:wght@400;700&display=swap">
<style>
  :root {
    --stage: #1f7d04;
    --card: #ffffff;
    --band: #3a3a3c;
    --ink: #2b2b2b;
    --brand-grey: #77787b;
    --accent: #e8262c;
    --tone-blue: #cfe2f3;
    --tone-yellow: #fbefc2;
    --tone-red: #f6cfcf;
    --tone-green: #cfe8d6;
  }
  html, body {
    margin: 0;
    padding: 0;
    width: 1200px;
    height: 1200px;
    overflow: hidden;
    background: var(--stage);
  }
  .canvas {
    position: relative;
    width: 1200px;
    height: 1200px;
  }
  .card {
    position: absolute;
    background: var(--card);
    overflow: hidden;
  }
  /* Front */
  .card-front {
    left: 212px; top: 130px;
    width: 800px; height: 445px;
  }
  .front-wordmark {
    position: absolute;
    left: 0; right: 0; top: 358px;
    text-align: center;
    font-family: "Questrial", sans-serif;
    color: var(--brand-grey);
    font-size: 40px;
    line-height: 40px;
    letter-spacing: -0.5px;
    text-transform: uppercase;
  }
  .front-wordmark .sub {
    display: block;
    font-size: 14px;
    line-height: 18px;
    letter-spacing: 1px;
    margin-top: 4px;
  }
  .front-wordmark .mark-square {
    display: block;
    width: 22px; height: 22px;
    margin: -200px auto 178px;
    background: var(--brand-grey);
  }
  /* Back */
  .card-back {
    left: 220px; top: 649px;
    width: 800px; height: 445px;
  }
  .side-band {
    position: absolute;
    left: 0; top: 0;
    width: 73px; height: 100%;
    background: var(--band);
  }
  .back-wordmark {
    position: absolute;
    left: 137px; top: 94px;
    font-family: "Questrial", sans-serif;
    color: var(--brand-grey);
    font-size: 20px;
    line-height: 22px;
    text-transform: uppercase;
    letter-spacing: 0.5px;
    display: flex;
    align-items: center;
    gap: 12px;
  }
  .back-wordmark .mark-square {
    width: 16px; height: 16px;
    background: var(--brand-grey);
  }
  .person {
    position: absolute;
    right: 90px; top: 120px;
    text-align: right;
    font-family: "Josefin Sans", sans-serif;
    font-size: 15px;
    letter-spacing: 3.5px;
    line-height: 22px;
  }
  .person-name { color: var(--ink); font-weight: 700; }
  .person-role { color: var(--accent); font-weight: 400; }
  .address {
    position: absolute;
    left: 137px; top: 213px;
    font-family: "Josefin Sans", sans-serif;
    font-size: 14px;
    letter-spacing: 2.6px;
    line-height: 21px;
    color: var(--ink);
    text-transform: uppercase;
    margin: 0;
    font-style: normal;
  }
  .contacts {
    position: absolute;
    left: 137px; top: 290px;
    list-style: none;
    margin: 0; padding: 0;
    font-family: "Josefin Sans", sans-serif;
    font-size: 14px;
    letter-spacing: 2.2px;
    color: var(--ink);
  }
  .contacts li {
    display: flex;
    align-items: center;
    height: 25px;
  }
  .contacts svg {
    width: 15px; height: 15px;
    margin-right: 22px;
    fill: none;
    stroke: var(--accent);
    stroke-width: 1.6;
  }
  .corner-artwork {
    position: absolute;
    left: 545px; top: 216px;
    width: 255px; height: 229px;
    background: linear-gradient(135deg, var(--tone-green) 0%, var(--tone-yellow) 35%, var(--tone-red) 65%, var(--tone-blue) 100%);
  }
</style>
</head>
<body>
<main class="canvas">
  <section class="card card-front" aria-label="Card front">
    <div class="front-wordmark">
      <span class="mark-square"></span>
      Harborline Frame
      <span class="sub">Construction</span>
    </div>
  </section>

  <section class="card card-back" aria-label="Card back">
    <div class="side-band"></div>

    <div class="back-wordmark">
      <span class="mark-square"></span>
      <span>Harborline Frame</span>
    </div>

    <div class="person">
      <div class="person-name">MARTA KELLAN</div>
      <div class="person-role">DIRECTOR</div>
    </div>

    <address class="address">
      Unit 3, 212-216 Kestrel<br>
      Road Harbour East
    </address>

    <ul class="contacts">
      <li>
        <svg viewBox="0 0 16 16" aria-hidden="true"><path d="M2 6c0-2 3-3 6-3s6 1 6 3v1h-3V5.5H5V7H2z"/><rect x="4" y="8" width="8" height="6" rx="1"/><circle cx="8" cy="11" r="1.3"/></svg>
        9305 2817
      </li>
      <li>
        <svg viewBox="0 0 16 16" aria-hidden="true"><rect x="4" y="1.5" width="8" height="4"/><rect x="1.5" y="5.5" width="13" height="6" rx="1"/><rect x="4" y="9.5" width="8" height="5"/></svg>
        9305 2841
      </li>
      <li>
        <svg viewBox="0 0 16 16" aria-hidden="true"><rect x="1.5" y="3.5" width="13" height="9"/><path d="M1.5 3.5L8 9l6.5-5.5"/></svg>
        marta@harborlineframe.com
      </li>
      <li>
        <svg viewBox="0 0 16 16" aria-hidden="true"><circle cx="8" cy="8" r="6"/><path d="M2 8h12M8 2c-2.5 3-2.5 9 0 12M8 2c2.5 3 2.5 9 0 12"/></svg>
        www.harborlineframe.com
      </li>
    </ul>

    <div class="corner-artwork" role="img" aria-label="Decorative corner artwork of the company symbol in soft multicolour tones"></div>
  </section>
</main>
</body>
</html>
```